Meditation for IVF and infertility

I need a flyer inviting IVF patients to join my Meditation class, I would like to offer free meditation to ivf women and for couples this class is free every Thursday night at 5 pm
2437 west harlow ave suite K Santa Barbara Ca 93142
quillbrook-stillness.com for more details

```html
<!DOCTYPE html>
<html lang="en">
<head>
<meta charset="utf-8">
<title>Quillbrook Stillness – Free Meditation Class Flyer</title>
<link rel="stylesheet" href="https://fonts.googleapis.com/css2?family=Great+Vibes&family=Montserrat:wght@400;600;700;800&display=swap">
<style>
  :root {
    --paper: #ffffff;
    --green: #4b8563;
    --green-deep: #3f7656;
    --green-light: #5b9473;
    --green-text: #4a8a5f;
    --ink: #3b3b3b;
    --ink-soft: #555555;
    --mist: #e4efec;
    --shadow: rgba(60, 60, 60, 0.45);
  }
  * { margin: 0; padding: 0; box-sizing: border-box; }
  html, body { width: 924px; height: 1200px; overflow: hidden; background: var(--paper); }
  .flyer {
    position: relative; width: 924px; height: 1200px; overflow: hidden;
    background: var(--paper);
    font-family: "Montserrat", Arial, sans-serif; color: var(--ink);
  }
  .flyer__shapes { position: absolute; inset: 0; }
  .site {
    position: absolute; left: 96px; top: 79px;
    display: flex; align-items: center; gap: 12px;
    color: #fff; font-weight: 600; font-size: 18px; letter-spacing: 0.2px;
  }
  .headline__lead {
    position: absolute; left: 150px; top: 350px;
    font-weight: 800; font-size: 54px; color: #fff; letter-spacing: 1px;
    text-shadow: 2px 3px 0 var(--shadow);
  }
  .headline__script {
    position: absolute; left: 88px; top: 300px;
    font-family: "Great Vibes", cursive; font-size: 250px; line-height: 1;
    color: #fff; text-shadow: 5px 8px 0 rgba(90, 90, 90, 0.5);
    white-space: nowrap;
  }
  .invite {
    position: absolute; left: 166px; top: 566px;
    font-size: 36px; line-height: 45px; text-transform: uppercase;
    font-weight: 400; color: var(--ink);
  }
  .invite strong { font-weight: 700; }
  .invite .accent { color: var(--green-text); font-weight: 700; }
  .schedule {
    position: absolute; right: 116px; top: 774px;
    text-align: right; color: #fff; text-transform: uppercase;
    font-size: 36px; line-height: 1.25; font-weight: 400;
  }
  .schedule strong { font-weight: 700; }
  .schedule .schedule__big { font-size: 84px; font-weight: 800; line-height: 1; letter-spacing: 1px; }
  .schedule .schedule__small { font-size: 36px; }
  .brand {
    position: absolute; left: 74px; top: 852px; width: 296px; height: 296px;
    border-radius: 50%; background: #fff; border: 3px solid #4a4a4a;
    display: flex; flex-direction: column; align-items: center; justify-content: center;
    font-weight: 600; font-size: 28px; line-height: 1.2; color: #4a4a4a; text-align: center;
  }
  .contact {
    position: absolute; left: 474px; top: 1060px;
    font-size: 19px; line-height: 29px; color: var(--ink-soft); text-transform: uppercase;
  }
  .contact__row { display: flex; align-items: flex-start; gap: 12px; }
  .contact__row svg { flex: none; margin-top: 5px; }
  .contact__indent { padding-left: 28px; }
  .contact strong { font-weight: 700; color: var(--ink); }
</style>
</head>
<body>
<main class="flyer">
  <svg class="flyer__shapes" viewBox="0 0 924 1200" width="924" height="1200">
    <defs>
      <linearGradient id="photo-tone" x1="0" y1="0" x2="0" y2="1">
        <stop offset="0" stop-color="#514d48"/>
        <stop offset="0.25" stop-color="#6c655c"/>
        <stop offset="0.45" stop-color="#8e9592"/>
        <stop offset="0.62" stop-color="#d2e2de"/>
        <stop offset="1" stop-color="#e9f3f0"/>
      </linearGradient>
      <linearGradient id="base-tone" x1="0" y1="0" x2="1" y2="0">
        <stop offset="0" stop-color="#ffffff"/>
        <stop offset="1" stop-color="#e4e4e4"/>
      </linearGradient>
    </defs>
    <g role="img" aria-label="Photo of a group of people seated on yoga mats in a bright studio, stretching with hands clasped behind their backs">
      <rect x="34" y="31" width="856" height="800" fill="url(#photo-tone)"/>
    </g>
    <rect x="34" y="980" width="856" height="195" fill="url(#base-tone)"/>
    <polygon points="0,850 924,1008 924,1200 0,1200" fill="#fff" opacity="0.6"/>
    <polygon points="0,796 924,725 924,1046 0,968" fill="var(--green)"/>
    <polygon points="0,796 330,771 120,968 0,968" fill="var(--green-deep)" opacity="0.5"/>
    <polygon points="620,748 924,725 924,880" fill="var(--green-light)"/>
    <polygon points="0,1165 400,1200 0,1200" fill="var(--green)"/>
  </svg>

  <div class="site">
    <svg width="20" height="20" viewBox="0 0 20 20" fill="none" stroke="#fff" stroke-width="1.6" aria-hidden="true">
      <circle cx="10" cy="10" r="8.5"/><ellipse cx="10" cy="10" rx="3.8" ry="8.5"/>
      <line x1="1.5" y1="10" x2="18.5" y2="10"/><path d="M3 5.5h14M3 14.5h14"/>
    </svg>
    quillbrook-stillness.com
  </div>

  <div class="headline__script">Invited</div>
  <div class="headline__lead">YOU’RE</div>

  <p class="invite">
    To join us for<br>
    <span class="accent">Free meditation class</span><br>
    To <strong>IVF women</strong> and<br>
    for <strong>couples</strong>
  </p>

  <p class="schedule">
    This class<br>
    <span class="schedule__small">is </span><span class="schedule__big">Free</span><br>
    Every <strong>Thursday</strong><br>
    Night <strong>at 5 PM</strong>
  </p>

  <div class="brand">
    <span>Quillbrook</span>
    <span>Stillness</span>
  </div>

  <div class="contact">
    <div class="contact__row">
      <svg width="16" height="20" viewBox="0 0 16 20" aria-hidden="true"><path d="M8 1a6.5 6.5 0 0 0-6.5 6.5C1.5 12 8 19 8 19s6.5-7 6.5-11.5A6.5 6.5 0 0 0 8 1z" fill="none" stroke="var(--green)" stroke-width="2.2"/><circle cx="8" cy="7.5" r="2.2" fill="var(--green)"/></svg>
      <span>2437 W Harlow Ave Suite K</span>
    </div>
    <div class="contact__indent">Santa Barbara, CA 93142</div>
    <div class="contact__row">
      <svg width="16" height="18" viewBox="0 0 24 24" aria-hidden="true"><path fill="var(--green)" d="M6.6 10.8a15.2 15.2 0 0 0 6.6 6.6l2.2-2.2c.3-.3.7-.4 1-.2 1.1.4 2.3.6 3.6.6.6 0 1 .4 1 1V20c0 .6-.4 1-1 1A17 17 0 0 1 3 4c0-.6.4-1 1-1h3.5c.6 0 1 .4 1 1 0 1.3.2 2.5.6 3.6.1.3 0 .7-.2 1z"/></svg>
      <strong>PH: (707) 555-0148</strong>
    </div>
  </div>
</main>
</body>
</html>
```